Halvik builders

Tarven Q480 year 2021 needs a full wrap. My companies name is Halvik Builders we are a high end landscape design build company. We specialize in pavers retaining walls, patio covers and decks.

```html
<!DOCTYPE html>
<html lang="en">
<head>
<meta charset="utf-8">
<title>Halvik Builders – Tarven Q480 Wrap</title>
<link rel="stylesheet" href="https://fonts.googleapis.com/css2?family=Marcellus&family=Montserrat:wght@600&display=swap">
<style>
  :root{
    --bg:#ffffff;
    --silver:#d9d9d9;
    --stripe:#f2f2f2;
    --gold:#e3a21e;
    --gold-deep:#c98414;
    --brown:#4a2a10;
    --brown-mid:#6b3c12;
    --slogan:#b9782a;
    --navy:#132c46;
    --cream:#fff6e6;
  }
  html,body{margin:0;padding:0;width:1200px;height:944px;overflow:hidden;background:var(--bg);}
  .wrap-sheet{display:block;width:1200px;height:944px;}
  .service-list{font-family:"Marcellus",serif;font-size:14px;fill:var(--navy);}
  .contact-url{font-family:"Marcellus",serif;font-size:15px;fill:var(--cream);}
  .contact-phone{font-family:"Marcellus",serif;font-size:20px;fill:var(--cream);}
  .slogan{font-family:"Marcellus",serif;fill:var(--slogan);}
  .slogan-top{font-size:17px;}
  .slogan-big{font-size:24px;}
  .brand-name{font-family:"Marcellus",serif;font-size:20px;fill:var(--navy);}
  .brand-tagline{font-family:"Montserrat",sans-serif;font-weight:600;font-size:7.4px;fill:var(--navy);letter-spacing:.2px;}
</style>
</head>
<body>
<svg class="wrap-sheet" viewBox="0 0 1200 944" xmlns="http://www.w3.org/2000/svg">
  <defs>
    <linearGradient id="bedGradientR" x1="0" x2="1" y1="0" y2="0">
      <stop offset="0" stop-color="var(--brown-mid)"/>
      <stop offset="1" stop-color="var(--gold-deep)"/>
    </linearGradient>
    <linearGradient id="bedGradientL" x1="1" x2="0" y1="0" y2="0">
      <stop offset="0" stop-color="var(--brown-mid)"/>
      <stop offset="1" stop-color="var(--gold-deep)"/>
    </linearGradient>
    <linearGradient id="goldGradient" x1="0" x2="0" y1="0" y2="1">
      <stop offset="0" stop-color="var(--gold)"/>
      <stop offset="1" stop-color="var(--gold-deep)"/>
    </linearGradient>
  </defs>

  <!-- Passenger side panel (front to the right) -->
  <g class="side-panel side-passenger">
    <path class="front-silver" d="M456 152 L880 152 L1150 175 L1150 330 L456 330 Z" fill="var(--silver)"/>
    <path class="cab-gold" d="M456 152 L540 152 L940 265 L940 330 L456 330 Z" fill="url(#goldGradient)"/>
    <path class="stripe" d="M540 152 L575 152 L945 255 L940 268 Z" fill="var(--stripe)"/>
    <path class="bed-amber" d="M58 166 L456 166 L456 326 L58 326 Z" fill="url(#bedGradientR)"/>
    <path class="bed-dark-sweep" d="M58 166 L200 166 Q330 200 410 326 L58 326 Z" fill="var(--brown)" opacity=".85"/>
    <circle class="wheel-arch" cx="265" cy="362" r="88" fill="var(--bg)"/>
    <circle class="wheel-arch" cx="1003" cy="362" r="88" fill="var(--bg)"/>

    <text class="slogan slogan-top" transform="translate(86 180) rotate(10)">It’s Time to Discover</text>
    <text class="slogan slogan-big" transform="translate(108 208) rotate(10)">Your Zen</text>
    <text class="contact-url" x="451" y="197" text-anchor="end">https://halvikbuilders.com</text>
    <text class="contact-phone" x="451" y="221" text-anchor="end">(206) 555-0148</text>

    <text class="service-list" x="532" y="228">~ Paver Patios</text>
    <text class="service-list" x="524" y="243">~ Paver Driveways</text>
    <text class="service-list" x="516" y="257">~ Retaining walls</text>
    <text class="service-list" x="507" y="272">~ Firepits &amp; Fireplaces</text>
    <text class="service-list" x="499" y="286">~ Decks &amp; Railings</text>
    <text class="service-list" x="491" y="301">~ Pools</text>

    <rect class="brand-square" x="749" y="238" width="20" height="20" fill="var(--navy)"/>
    <text class="brand-name" x="759" y="278" text-anchor="middle">Halvik Builders</text>
    <text class="brand-tagline" x="759" y="288" text-anchor="middle">OUTDOOR LIVING SPACES</text>
  </g>

  <!-- Driver side panel (front to the left) -->
  <g class="side-panel side-driver">
    <path class="front-silver" d="M55 660 L320 630 L740 630 L740 810 L55 810 Z" fill="var(--silver)"/>
    <path class="cab-gold" d="M265 760 L650 640 L740 640 L740 810 L265 810 Z" fill="url(#goldGradient)"/>
    <path class="stripe" d="M265 752 L640 632 L672 632 L270 764 Z" fill="var(--stripe)"/>
    <path class="bed-amber" d="M740 644 L1150 644 L1150 807 L740 807 Z" fill="url(#bedGradientL)"/>
    <path class="bed-dark-sweep" d="M1150 644 L1010 644 Q870 690 780 807 L1150 807 Z" fill="var(--brown)" opacity=".85"/>
    <circle class="wheel-arch" cx="196" cy="848" r="88" fill="var(--bg)"/>
    <circle class="wheel-arch" cx="934" cy="848" r="88" fill="var(--bg)"/>

    <text class="contact-url" x="750" y="674">https://halvikbuilders.com</text>
    <text class="contact-phone" x="750" y="698">(206) 555-0148</text>
    <text class="slogan slogan-top" transform="translate(921 700) rotate(-13)">It’s Time to Discover</text>
    <text class="slogan slogan-big" transform="translate(982 714) rotate(-13)">Your Zen</text>

    <text class="service-list" x="546" y="706">~ Paver Patios</text>
    <text class="service-list" x="554" y="721">~ Paver Driveways</text>
    <text class="service-list" x="562" y="736">~ Retaining walls</text>
    <text class="service-list" x="571" y="750">~ Firepits &amp; Fireplaces</text>
    <text class="service-list" x="579" y="765">~ Decks &amp; Railings</text>
    <text class="service-list" x="587" y="780">~ Pools</text>

    <rect class="brand-square" x="416" y="718" width="20" height="20" fill="var(--navy)"/>
    <text class="brand-name" x="426" y="759" text-anchor="middle">Halvik Builders</text>
    <text class="brand-tagline" x="426" y="769" text-anchor="middle">OUTDOOR LIVING SPACES</text>
  </g>
</svg>
</body>
</html>
```